Webdesign für Software Ingenieurbüro
Vielen Dank für das professionelle Design, Umsetzung mit WordPress und rasche Reaktionszeiten. MondscheinKobold geht die Extrameile.
Zielgruppe
English text below
Meine Firma erstellt Software und bietet sämtliche Dienstleistungen rund um die Softwareentwicklung an.
Die Zielgruppe sind Auftraggeber, welche Software-Engineering/Entwicklungsaufträge vergeben.
English
My company creates software and offers all services related to software development.
The target group are those who award software engineering / development contracts.
Aufgabenstellung
Die bestehende Seite www.tarnvok-systems.ch soll neu und modern designed werden. Die Struktur der Seite (Menuunterteilung) kann (muss aber nicht zwingend) übernommen werden.
Das Logo kann, muss aber nicht übernommen werden.
Ev. als OnePage-Seite gestalten.
Responsive-Design ist zwingend, d.h. die Seite muss sowohl auf dem Desktop wie auch auf dem Mobile-Gerät ansprechend aussehen.
Zur Illustration soll auf Fotos verzichtet werden. Aber es können sehr gerne Vektorgrafiken für die Illustration und/oder Icons verwendet werden.
Link auf Social-Media Qorvu muss vorhanden sein.
Der persönliche Kontakt zum Kunden ist mir wichtig, deshalb sollte mein Foto vorhanden sein. Ev. nicht so prominent wie auf der aktuellen Seite.
Die Umsetzung wird mit Wordpress und einem Standard-Theme geschehen. Falls Sie Wordpress kennen, können Sie das Theme angeben, mit welchem sich die Seite umsetzen lässt.
The existing site www.tarnvok-systems.ch is to be redesigned and modernized. The structure of the page (menu subdivision) can (but does not have to be) mandatory.
The logo can, but does not have to be adopted.
Ev. as a OnePage page.
Responsive design is required, the page must look appealing both on the desktop and on the mobile device.
For the illustration, photographs are not desired. But vector graphics can be used for illustration and / or icons.
Link to social media Qorvu must be available.
Personal contact with the customer is important to me, so my photo should be available. Ev. not as prominent as on the current page.
The implementation will be done with Wordpress and a standard theme. If you are familiar with Wordpress, you can specify the theme with which the page can be implemented.

```html
<!DOCTYPE html>
<html lang="de">
<head>
<meta charset="utf-8">
<title>Tarnvok Systems – Professionelle Softwareentwicklung</title>
<link href="https://fonts.googleapis.com/css2?family=Roboto:ital,wght@0,500;1,900&family=Source+Sans+3:wght@400;600&display=swap" rel="stylesheet">
<style>
:root{
  --navy:#0a2f7a;
  --blue-deep:#0b3a8f;
  --blue-bright:#1670c4;
  --accent:#3e7de0;
  --accent-line:#6f9fd8;
  --ink:#444a52;
  --label:#1d4c9c;
  --text-soft:#585f68;
  --panel:#f2f5f8;
  --frame:#f7f8f9;
  --footer:#0b1d46;
  --white:#ffffff;
}
*{margin:0;padding:0;box-sizing:border-box}
html,body{width:850px;height:1200px;overflow:hidden}
body{position:relative;background:var(--white);font-family:"Source Sans 3",sans-serif;color:var(--ink)}
.abs{position:absolute}
.heading{font-family:"Roboto",sans-serif;font-style:italic;font-weight:900;font-size:18px;line-height:18px;text-align:center}
.rule{position:absolute;height:1px;width:31px;background:var(--accent-line);left:409px}
.btn{position:absolute;display:flex;align-items:center;justify-content:center;border-radius:11px;background:var(--accent);color:var(--white);font-family:"Roboto",sans-serif;font-weight:500;font-size:7px;letter-spacing:.1px;box-shadow:0 2px 5px rgba(20,60,140,.3)}

/* hero */
.hero{left:0;top:0;width:850px;height:331px;background:linear-gradient(120deg,var(--navy) 0%,var(--blue-deep) 45%,var(--blue-bright) 100%)}
.brand{left:56px;top:14px;display:flex;align-items:center;gap:4px;color:var(--white);font-weight:600;font-size:10px}
.brand-mark{width:12px;height:12px;border:1.5px solid var(--white);border-radius:50%}
.nav{top:24px;left:500px;display:flex;gap:0;font-size:7.5px;color:var(--white)}
.nav a{color:var(--white);text-decoration:none;position:absolute;white-space:nowrap}
.nav .active::after{content:"";position:absolute;left:-1px;right:-1px;top:12px;height:1px;background:#7fd0ff}
.nav-divider{left:722px;top:25px;width:1px;height:8px;background:rgba(255,255,255,.7)}
.social{display:flex;gap:6px;font-size:6.5px;color:var(--white)}
.social span{border:1px solid currentColor;padding:1px 2px;line-height:7px}
.hero-title{left:166px;top:114px;color:var(--white);font-family:"Roboto",sans-serif;font-style:italic;font-weight:900;font-size:18px;line-height:18px}
.hero-text{left:166px;top:165px;width:238px;color:rgba(255,255,255,.88);font-size:8.4px;line-height:11.5px;text-align:justify}
.hero-art{left:403px;top:99px;width:322px;height:168px;border-radius:6px;background:linear-gradient(135deg,rgba(40,100,200,.35),rgba(20,70,170,.15))}

/* method */
.method-title{left:0;top:387px;width:850px;color:var(--ink)}
.method-item{position:absolute;top:447px;width:120px;text-align:center}
.method-icon{width:42px;height:42px;margin:0 auto;border-radius:8px;background:linear-gradient(135deg,#3a67c6,#1d3f94);opacity:.85}
.method-label{margin-top:25px;color:var(--label);font-size:10px;line-height:12.5px}

/* technology frame */
.device{left:166px;top:646px;width:518px;height:282px;border:1px solid #dfe2e6;border-bottom:none;border-radius:16px 16px 0 0;background:var(--frame);box-shadow:0 0 14px rgba(0,0,0,.05)}
.device-btn{left:182px;top:838px;width:14px;height:14px;border-radius:50%;background:#fbfbfb}
.device-btn::after{content:"";position:absolute;left:4px;top:4px;width:6px;height:6px;border:1px solid #c9ccd0;border-radius:1px}
.device-cam{left:660px;top:844px;width:5px;height:5px;border-radius:50%;background:#8b9098}
.screen{left:209px;top:685px;width:430px;height:243px;background:var(--panel);border:1px solid #e2e6ea;border-bottom:none}
.tech-title{left:209px;top:719px;width:430px;color:var(--ink)}
.tech-text{left:209px;top:801px;width:445px;text-align:center;color:var(--text-soft);font-size:7.5px;line-height:10.5px}
.tech-grid{left:230px;top:850px;width:400px;display:grid;grid-template-columns:repeat(4,1fr);row-gap:14px;text-align:center;font-size:9.5px;font-weight:600}
.t-red{color:#d23a32}.t-dark{color:#333a44}.t-green{color:#5aa33a}.t-blue{color:#1a2fd0}.t-gray{color:#6a6f76}

/* contact */
.contact{left:0;top:928px;width:850px;height:223px;background:linear-gradient(120deg,#0a2a72,#0a3b95 60%,#0d47a6)}
.contact-title{left:0;top:961px;width:850px;color:var(--white)}
.contact-text{left:0;top:1021px;width:850px;text-align:center;color:rgba(255,255,255,.9);font-size:7.5px;line-height:10.5px}
.footer{left:0;top:1151px;width:850px;height:49px;background:var(--footer);color:rgba(255,255,255,.85);font-size:5.5px;display:flex;align-items:center;justify-content:center}
</style>
</head>
<body>

<header class="abs hero"></header>
<div class="abs brand"><span class="brand-mark"></span>Tarnvok Systems</div>
<nav class="abs nav">
  <a class="active" style="left:0">Home</a>
  <a style="left:45px">Dienstleistungen</a>
  <a style="left:126px">Firma</a>
  <a style="left:171px">Kontakt</a>
</nav>
<div class="abs nav-divider"></div>
<div class="abs social" style="left:745px;top:24px"><span>Lynkra</span><span>Qorvu</span><span>Fazbo</span></div>

<h1 class="abs hero-title">Professionelle<br>Softwareentwicklung</h1>
<p class="abs hero-text">Tarnvok Systems stellt unter Verwendung modernster Technologien und leichtgewichtiger Prozessen qualitativ hochstehende Software her.</p>
<a class="btn" style="left:166px;top:215px;width:123px;height:20px">HABEN SIE EIN PROJEKT?</a>
<div class="abs hero-art" role="img" aria-label="Linienillustration aus Browserfenstern, Stoppuhr, Diagramm und Lupe"></div>

<h2 class="abs heading method-title">Unsere Methodik</h2>
<div class="rule" style="top:425px"></div>
<div class="method-item" style="left:165px"><div class="method-icon" role="img" aria-label="Eulen-Icon"></div><p class="method-label">Teamführung und<br>Coaching</p></div>
<div class="method-item" style="left:298px"><div class="method-icon" role="img" aria-label="Stoppuhr-Icon"></div><p class="method-label">Scrum und Extreme<br>Programming</p></div>
<div class="method-item" style="left:431px"><div class="method-icon" role="img" aria-label="Geräte-Icon"></div><p class="method-label">Continuous Integration/<br>Delivery</p></div>
<div class="method-item" style="left:562px"><div class="method-icon" role="img" aria-label="Steuerrad-Icon"></div><p class="method-label">Application Lifecylce<br>Management</p></div>
<a class="btn" style="left:375px;top:567px;width:100px;height:21px">LASS UNS START</a>

<div class="abs device"></div>
<div class="abs device-btn"></div>
<div class="abs device-cam"></div>
<section class="abs screen"></section>
<h2 class="abs heading tech-title">Konzentrieren Sie sich<br>auf Technologie</h2>
<div class="rule" style="top:780px"></div>
<p class="abs tech-text">Über 18 Jahre Erfahrung in der Softwareentwicklung und Entwicklung von<br>Backendsystemen mit hohem Transaktionsaufkommen</p>
<div class="abs tech-grid">
  <span class="t-red">Kavra</span>
  <span class="t-dark">QuellDB</span>
  <span class="t-green">Lenzio</span>
  <span class="t-dark">Ecklar</span>
  <span class="t-red">Orvantis</span>
  <span class="t-blue">&lt;xml /&gt;</span>
  <span class="t-gray">Schlafwerk</span>
  <span class="t-green">Seifpanel</span>
</div>

<section class="abs contact"></section>
<h2 class="abs heading contact-title">Sie können eine Frage stellen</h2>
<div class="rule" style="top:1001px"></div>
<p class="abs contact-text">Ich freue mich auf Ihre Nachricht. Füllen Sie bitte untenstehendes Formular aus.<br>Ich werde so rasch wie möglich mit Ihnen in Kontakt treten.</p>
<div class="abs social" style="left:393px;top:1065px"><span>Lynkra</span><span>Qorvu</span><span>Fazbo</span></div>
<a class="btn" style="left:369px;top:1098px;width:115px;height:20px">SCHREIBEN NACHRICHT</a>

<footer class="abs footer">© Copyright 2010 - 2017 Tarnvok Systems GmbH. All rights reserved.</footer>

</body>
</html>
```